Water Filtration Company needs a business card design using our existing logo/colours!

We design and manufacture and export specialised water filtration equipment. Our equipment will take unclean dirty water and filters to safe clean drinkable water.
We would like to see designs using our existing logo and colours (see attached "Palette") that represents clean safe drinking water (fresh, clean designs but still professional and modern). Our customers are other businesses who supply water filtration equipment, governments, and private individuals.
BUSINESS CARD DETAILS (Common details):
Tel: + 61 7 55 419 276
www: brindlepeak.com.au
Address: 3/47 Cordwell Parade
Marlow Flats NSW 2593 Australia
(please include the word Australia as we are an international company)
Must include: COMMERCIAL WATER FILTRATION EQUIPMENT
NAME NO 1:
Owen Pritch
General Manager
Mobile: +61 427 38 91 04
Email: owen@brindlepeak.com.au
NAME NO. 2:
Gina Rosk
Business Manager
Mobile: +61 409 572 148
Email: gina@brindlepeak.com.au
Must Have:
1) PRINT READY IN .AI & .PDF FORMATS
2) Also saved in file format .ai (Adobe Illustrator - compatible with CS4)
3) Use existing LOGO & COLOURS: Please use our logo (see attached file)
4) FONTS: we have used Avenir & Helvetica in the past but are open to other font types for the address etc.
Thank you!

```html
<!DOCTYPE html>
<html lang="en">
<head>
<meta charset="utf-8">
<title>Brindle Peak – Business Card</title>
<link rel="stylesheet" href="https://fonts.googleapis.com/css2?family=Roboto+Condensed:wght@400;700&display=swap">
<style>
  :root {
    --bg: #e9ecee;
    --teal-deep: #0e6f8c;
    --teal: #1596b4;
    --teal-light: #7fcfe0;
    --water-pale: #cfeef5;
    --ink: #2a2a2a;
    --slate: #4f7683;
    --white: #ffffff;
  }
  * { margin: 0; padding: 0; box-sizing: border-box; }
  html, body { width: 1200px; height: 918px; overflow: hidden; }
  body {
    background: var(--bg);
    font-family: "Roboto Condensed", "Arial Narrow", sans-serif;
    display: flex; flex-direction: column; align-items: center; justify-content: center;
    gap: 38px;
  }
  .card {
    position: relative; width: 700px; height: 400px; overflow: hidden;
    box-shadow: 0 6px 18px rgba(0,0,0,.18);
  }

  /* Back side */
  .card--back {
    background: linear-gradient(160deg, var(--teal) 0%, var(--teal-deep) 100%);
  }
  .card--back .water {
    position: absolute; left: 0; bottom: 0; width: 100%; height: 190px;
    background: linear-gradient(175deg, rgba(207,238,245,0) 0%, rgba(207,238,245,.55) 45%, rgba(127,207,224,.8) 100%);
  }
  .card--back .tagline-band {
    position: absolute; left: 0; top: 222px; width: 100%; height: 34px;
    background: rgba(255,255,255,.35);
    display: flex; align-items: center; padding-left: 40px;
    color: #5d6c72; font-weight: 700; font-size: 22px; letter-spacing: 2px;
  }
  .card--back .brand {
    position: absolute; left: 40px; top: 60px; display: flex; align-items: center; gap: 18px;
    color: var(--white); font-weight: 700; font-size: 92px; line-height: 1;
  }
  .brand-dot { width: 30px; height: 30px; border-radius: 50%; background: currentColor; }

  /* Front side */
  .card--front { background: var(--white); }
  .card--front .water {
    position: absolute; left: 0; bottom: 0; width: 100%; height: 110px;
    background: linear-gradient(180deg, rgba(207,238,245,0) 0%, var(--water-pale) 40%, var(--teal-light) 100%);
  }
  .divider {
    position: absolute; left: 352px; top: 40px; width: 1.5px; height: 270px; background: var(--slate);
  }
  .company {
    position: absolute; left: 34px; top: 40px; width: 300px;
  }
  .company .brand {
    display: flex; align-items: center; gap: 10px; justify-content: flex-end;
    color: var(--teal-deep); font-weight: 700; font-size: 48px; line-height: 1;
  }
  .company .brand-dot { width: 16px; height: 16px; }
  .company .tagline {
    margin-top: 14px; color: var(--ink); font-weight: 700; font-size: 14.5px; letter-spacing: .4px;
  }
  .address {
    margin-top: 18px; margin-left: 70px; color: var(--slate); font-size: 20px; line-height: 1.15; font-style: normal;
  }
  .contact {
    position: absolute; right: 30px; top: 95px; text-align: right; color: var(--ink);
  }
  .contact .name { color: var(--teal); font-size: 34px; font-weight: 400; line-height: 1; }
  .contact .role { color: var(--teal); font-size: 15px; margin-bottom: 18px; }
  .contact .line { font-size: 22px; line-height: 1.2; }
  .contact .web { color: var(--teal-deep); font-weight: 700; font-size: 23px; margin-top: 10px; }
</style>
</head>
<body>
  <section class="card card--back" aria-label="Business card back">
    <div class="water" role="img" aria-label="Clear water surface with splash and bubbles"></div>
    <div class="brand"><span>Brindle Peak</span><span class="brand-dot"></span></div>
    <div class="tagline-band">COMMERCIAL WATER FILTRATION EQUIPMENT</div>
  </section>

  <section class="card card--front" aria-label="Business card front">
    <div class="water" role="img" aria-label="Clear water wave with droplet and bubbles"></div>
    <div class="company">
      <div class="brand"><span>Brindle Peak</span><span class="brand-dot"></span></div>
      <p class="tagline">COMMERCIAL WATER FILTRATION EQUIPMENT</p>
      <address class="address">3/47 Cordwell Parade<br>Marlow Flats<br>NSW 2593<br>Australia</address>
    </div>
    <div class="divider"></div>
    <div class="contact">
      <p class="name">Owen Pritch</p>
      <p class="role">General Manager</p>
      <p class="line">T: + 61 7 55 419 276</p>
      <p class="line">M: +61 427 38 91 04</p>
      <p class="line">owen@brindlepeak.com.au</p>
      <p class="web">www.brindlepeak.com.au</p>
    </div>
  </section>
</body>
</html>
```